I am a new company with the latest technology in the concrete polishing business

We need a logo design for a new company out of Toronto, Canada. We polish residential, commercial and industrial concrete as well as different epoxy toppings.

Target Market(s)

How Owners with expendable incomes

Industry/Entity Type

Construction

Contact Information for Business Card

be able to see content rather easily

Colors
0355a3
fbed22
1b1b1b

Requirements
Must have
• simple and elegant

```html
<!DOCTYPE html>
<html lang="en">
<head>
<meta charset="utf-8">
<title>Slabline Polish – Business Card</title>
<link href="https://fonts.googleapis.com/css2?family=Roboto+Condensed:wght@700&family=Rajdhani:wght@600&display=swap" rel="stylesheet">
<style>
  :root {
    --brand-blue: #0355a3;
    --tab-blue: #3a56a8;
    --ink: #1b1b1b;
    --steel-dark: #5a5a5a;
    --steel-light: #b9b9b9;
    --card: #ffffff;
    --backdrop: #e7e4df;
  }
  * { margin: 0; padding: 0; box-sizing: border-box; }
  html, body { width: 900px; height: 1200px; overflow: hidden; }
  body { background: var(--backdrop); position: relative; }

  .card {
    position: absolute;
    left: 87px;
    width: 733px;
    height: 428px;
    background: var(--card);
    border-radius: 24px;
    overflow: hidden;
    box-shadow: 0 6px 14px rgba(0,0,0,.25);
  }
  .card--front { top: 137px; }
  .card--back { top: 633px; }

  .name-tab {
    position: absolute; left: 0; top: 0;
    width: 410px; height: 101px;
  }
  .name-tab__label {
    position: absolute; left: 48px; top: 34px;
    font: 700 31px "Roboto Condensed", sans-serif;
    color: #fff; letter-spacing: .3px;
  }

  .wordmark {
    position: absolute;
    font-family: "Roboto Condensed", sans-serif;
    font-weight: 700;
    color: var(--brand-blue);
    text-transform: uppercase;
    line-height: 1;
  }
  .wordmark span { display: block; }
  .wordmark--front { left: 48px; top: 170px; font-size: 54px; }
  .wordmark--back { left: 0; right: 0; top: 145px; text-align: center; font-size: 70px; }

  .contact-list {
    position: absolute; left: 406px; top: 140px;
    list-style: none;
  }
  .contact-item {
    display: flex; gap: 5px; margin-bottom: 12px;
  }
  .contact-icon {
    width: 32px; flex: none;
    background: var(--tab-blue);
    border-radius: 6px;
    display: flex; align-items: center; justify-content: center;
  }
  .contact-text {
    width: 253px; min-height: 28px;
    border-radius: 6px;
    background: linear-gradient(90deg, var(--steel-dark), var(--steel-light) 55%, var(--steel-dark));
    color: #fff;
    font: 600 17px "Rajdhani", sans-serif;
    letter-spacing: 1.2px;
    text-transform: uppercase;
    padding: 3px 8px;
    line-height: 22px;
  }
  .contact-item--address .contact-text { min-height: 64px; padding-top: 9px; }

  .card-footer-band {
    position: absolute; left: 0; bottom: 0;
    width: 100%; height: 25px;
    background: linear-gradient(90deg, var(--steel-dark), var(--steel-light) 55%, var(--steel-dark));
  }
</style>
</head>
<body>

<section class="card card--front" aria-label="Business card front">
  <svg class="name-tab" viewBox="0 0 410 101" aria-hidden="true">
    <polygon points="0,0 410,0 320,101 0,101" fill="var(--tab-blue)"/>
  </svg>
  <p class="name-tab__label">YOUR NAME HERE</p>

  <h1 class="wordmark wordmark--front"><span>Slabline</span><span>Polish</span></h1>

  <ul class="contact-list">
    <li class="contact-item">
      <span class="contact-icon">
        <svg width="18" height="18" viewBox="0 0 24 24" aria-hidden="true"><path fill="#fff" d="M6.6 10.8a15 15 0 0 0 6.6 6.6l2.2-2.2c.3-.3.7-.4 1-.2 1.1.4 2.3.6 3.6.6.6 0 1 .4 1 1V20c0 .6-.4 1-1 1A17 17 0 0 1 3 4c0-.6.4-1 1-1h3.5c.6 0 1 .4 1 1 0 1.3.2 2.5.6 3.6.1.3 0 .7-.2 1z"/></svg>
      </span>
      <span class="contact-text">780.555.0147</span>
    </li>
    <li class="contact-item">
      <span class="contact-icon">
        <svg width="18" height="18" viewBox="0 0 24 24" aria-hidden="true"><path fill="#fff" d="M6 2h12v5H6zM3 8h18a1 1 0 0 1 1 1v8h-4v-3H6v3H2V9a1 1 0 0 1 1-1zm4 7h10v7H7z"/></svg>
      </span>
      <span class="contact-text">780.555.0193</span>
    </li>
    <li class="contact-item">
      <span class="contact-icon">
        <svg width="20" height="16" viewBox="0 0 24 18" aria-hidden="true"><rect x="1" y="1" width="22" height="16" fill="none" stroke="#fff" stroke-width="2"/><path d="M1 1l11 9 11-9" fill="none" stroke="#fff" stroke-width="2"/></svg>
      </span>
      <span class="contact-text">hello@slablinepolish.ca</span>
    </li>
    <li class="contact-item contact-item--address">
      <span class="contact-icon">
        <svg width="16" height="22" viewBox="0 0 16 22" aria-hidden="true"><path fill="none" stroke="#fff" stroke-width="2" d="M8 21s7-8 7-13A7 7 0 0 0 1 8c0 5 7 13 7 13z"/><circle cx="8" cy="8" r="2.5" fill="#fff"/></svg>
      </span>
      <span class="contact-text">2218-48B Street<br>Westbrook, Alberta T4X 1K7</span>
    </li>
  </ul>

  <div class="card-footer-band"></div>
</section>

<section class="card card--back" aria-label="Business card back">
  <h2 class="wordmark wordmark--back"><span>Slabline</span><span>Polish</span></h2>
</section>

</body>
</html>
```